Business Card Design Project

In addition to the logo design we want a professional and contemporary business card for a talent management agency. We provide management services to creative artists and want to communicate a professional creative vibe.
Updates

Project Deadline Extended
Reason: Sorry didnt realise I had put such a short timeline on it.

Target Market(s)

The business deals with creative artists and other industry professionals

Industry/Entity Type

Artists

Colors

Designer to choose colors to be used in the design.

Requirements
Must have
• Logo
Address
Phone
Email

```html
<!DOCTYPE html>
<html lang="en">
<head>
<meta charset="utf-8">
<title>Norvale Artists — Business Card</title>
<link rel="stylesheet" href="https://fonts.googleapis.com/css2?family=Open+Sans:ital,wght@0,400;0,600;0,700;1,400&display=swap">
<style>
  :root {
    --backdrop: #2a2b2d;
    --card: #1b1b1d;
    --card-edge: #3a3b3e;
    --text-light: #e6e7e8;
    --text-muted: #9c9ea1;
    --accent-green: #6bbf9a;
    --accent-grey: #a7a9ab;
    --silver: #c9cbce;
  }
  * { box-sizing: border-box; margin: 0; padding: 0; }
  html, body {
    width: 1200px; height: 1200px; overflow: hidden;
    background: var(--backdrop);
    font-family: "Open Sans", Arial, sans-serif;
  }
  .sheet { position: relative; width: 1200px; height: 1200px; }

  .card {
    position: absolute; left: 250px;
    width: 700px; height: 400px;
    background: var(--card);
    border: 1px solid var(--card-edge);
    box-shadow: 0 18px 40px rgba(0,0,0,.45);
  }
  .card--front { top: 110px; }
  .card--back { top: 570px; }

  .wordmark {
    position: absolute; left: 0; right: 0; top: 170px;
    text-align: center;
    font-weight: 700; font-size: 44px; letter-spacing: 1px;
    color: var(--silver);
  }

  .contact {
    position: absolute; left: 70px; top: 150px;
    display: flex; align-items: flex-start; gap: 26px;
  }
  .contact__mark {
    width: 56px; height: 56px; border-radius: 8px;
    background: var(--accent-grey); margin-top: 4px;
  }
  .contact__name {
    font-weight: 700; font-size: 28px; color: var(--text-light); line-height: 1.1;
  }
  .contact__name .surname { color: var(--accent-green); }
  .contact__role {
    font-style: italic; font-weight: 400; font-size: 18px; color: var(--text-muted);
  }
  .contact__list { list-style: none; margin-top: 12px; }
  .contact__list li {
    display: flex; align-items: center; gap: 12px;
    font-size: 15px; color: var(--text-light); line-height: 1.75;
  }
  .contact__list li::before {
    content: ""; width: 8px; height: 8px; background: var(--accent-green); flex: none;
  }

  .finish {
    position: absolute; left: 250px; top: 1045px;
    display: flex; align-items: center; gap: 14px;
  }
  .finish__label { font-size: 16px; color: var(--text-light); margin-right: 12px; }
  .swatch { width: 38px; height: 38px; }
  .swatch--green { background: var(--accent-green); }
  .swatch--grey { background: var(--accent-grey); }
</style>
</head>
<body>
<main class="sheet">
  <section class="card card--front" aria-label="Card front">
    <div class="wordmark">Norvale Artists</div>
  </section>

  <section class="card card--back" aria-label="Card back">
    <div class="contact">
      <div class="contact__mark"></div>
      <div class="contact__details">
        <p class="contact__name">Mara <span class="surname">Linden</span> <span class="contact__role">/ Manager</span></p>
        <ul class="contact__list">
          <li>14 Fern Lane, Westbrook NSW 2099 Australia</li>
          <li>Tel (+61 2) 5550 1427</li>
          <li>info@norvaleartists.com</li>
        </ul>
      </div>
    </div>
  </section>

  <div class="finish">
    <span class="finish__label">Silver spot UV</span>
    <span class="swatch swatch--green"></span>
    <span class="swatch swatch--grey"></span>
  </div>
</main>
</body>
</html>
```